Print on top the name of the company: (Or Similar)
Larkmoor Cleaning & Disinfecting
Because your standards aren't standard.

We adhere to ALL NVB guidelines for both residential and commercial cleaning.

Infection Control is our ultimate goal.

Instructions:
Opening a residential and commercial cleaning and disinfecting company in south Florida.

Targeting high-end residential clients, commercial and healthcare facilities, specializing in Ambulatory Care Guidelines. With a concentration and expertise in targeting Covid 19 and other transmissible pathogens.

UMRE trained.
Owned and operated by a licensed BSN Registered Nurse specially ​trained in Infection Control Prevention with over 25 years experience. Over two decades in Ambulatory Surgery Center Administration, Director of Nursing and Infection Control Prevention ad Consulting.

Looking to create a business flier that emphasizes Cleaning & Disinfection
along with the standard expectation for residential and Commercial cleaning services
Updates

Need extra days to review

Target Market(s)

Residential & Commercial

Font styles to use
Decorative

Requirements
Must have
• A checklist for cleaning services

```html
<!DOCTYPE html>
<html lang="en">
<head>
<meta charset="utf-8">
<title>Larkmoor Cleaning &amp; Disinfecting – Flyer</title>
<link href="https://fonts.googleapis.com/css2?family=Oswald:wght@400;500;600&family=Open+Sans:ital,wght@0,400;0,600;0,700;1,700&display=swap" rel="stylesheet">
<style>
  :root {
    --blue-deep: #0d4f96;
    --blue-mid: #1c6fc0;
    --blue-bright: #2a86d8;
    --blue-text: #1f5fae;
    --green: #8cc63f;
    --green-dark: #6fae2a;
    --ink: #2b2b2b;
    --grey-text: #4a4a4a;
    --paper: #ffffff;
  }
  * { box-sizing: border-box; margin: 0; padding: 0; }
  html, body { width: 1009px; height: 1200px; overflow: hidden; background: var(--paper); }
  .flyer { position: relative; width: 1009px; height: 1200px; overflow: hidden; background: var(--paper); font-family: "Open Sans", Arial, sans-serif; }
  .backdrop { position: absolute; inset: 0; }

  .brand-title {
    position: absolute; right: 36px; top: 50px; width: 400px;
    text-align: right; color: #fff;
    font-family: "Oswald", "Arial Narrow", sans-serif; font-weight: 500;
    font-size: 60px; line-height: 72px; letter-spacing: 1px; text-transform: uppercase;
  }
  .brand-rule { position: absolute; left: 687px; top: 286px; width: 280px; height: 4px; background: #fff; }
  .tagline {
    position: absolute; right: 44px; top: 318px; width: 340px;
    text-align: right; color: #fff; font-size: 27px; line-height: 34px;
  }

  .goal {
    position: absolute; right: 38px; top: 514px;
    font-family: "Oswald", "Arial Narrow", sans-serif; font-weight: 500;
    font-size: 32px; color: var(--blue-text); text-transform: uppercase; letter-spacing: .3px;
  }
  .goal-note {
    position: absolute; right: 38px; top: 558px; width: 580px; text-align: right;
    font-weight: 700; font-size: 19px; line-height: 24px; color: var(--ink);
  }

  .service-column { position: absolute; top: 636px; }
  .service-column.commercial { left: 66px; width: 400px; }
  .service-column.residential { left: 560px; width: 408px; }
  .column-head { position: relative; height: 44px; }
  .column-head svg { position: absolute; left: 0; top: 0; overflow: visible; }
  .column-head h2 {
    position: absolute; left: 92px; top: 0; line-height: 46px;
    font-family: "Oswald", "Arial Narrow", sans-serif; font-weight: 500;
    font-size: 32px; color: #fff; text-transform: uppercase; letter-spacing: .5px;
  }
  .service-list { list-style: none; margin-top: 18px; }
  .service-list li {
    display: flex; align-items: center; height: 36.4px;
    font-size: 23px; color: var(--grey-text);
  }
  .service-list .tick {
    width: 27px; height: 27px; margin-right: 20px; flex: none;
    border: 2px solid var(--blue-mid); border-radius: 4px; background: #eaf2fb;
    display: flex; align-items: center; justify-content: center;
  }
  .service-list.commercial-list .tick { margin-left: 16px; }
  .service-list.residential-list .tick { margin-left: 28px; }

  .column-divider { position: absolute; left: 512px; top: 640px; width: 2px; height: 306px; background: #c9d3de; }

  .credentials {
    position: absolute; left: 200px; top: 994px; width: 640px; text-align: center;
    font-style: italic; font-weight: 700; font-size: 13.5px; line-height: 19px; color: var(--blue-text);
  }

  .website {
    position: absolute; left: 74px; top: 1148px;
    font-family: "Oswald", "Arial Narrow", sans-serif; font-weight: 500; font-size: 22px; color: #fff;
  }
  .estimate {
    position: absolute; left: 584px; top: 1086px; width: 390px; text-align: center;
    font-family: "Oswald", "Arial Narrow", sans-serif; font-weight: 500; font-size: 27px; color: #fff;
  }
  .call {
    position: absolute; left: 548px; top: 1138px; display: flex; align-items: center; gap: 14px;
    font-family: "Oswald", "Arial Narrow", sans-serif; font-weight: 400; font-size: 36px; color: #fff;
  }
  .call .number { font-weight: 500; }
</style>
</head>
<body>
<main class="flyer">
  <svg class="backdrop" width="1009" height="1200" viewBox="0 0 1009 1200">
    <defs>
      <linearGradient id="photoTone" x1="0" y1="0" x2="1" y2="1">
        <stop offset="0" stop-color="#dfe3e8"/>
        <stop offset=".55" stop-color="#eef0f2"/>
        <stop offset="1" stop-color="#c8ced6"/>
      </linearGradient>
      <linearGradient id="teamTone" x1="0" y1="0" x2="1" y2="1">
        <stop offset="0" stop-color="#e9e2d4"/>
        <stop offset=".5" stop-color="#a9b88a"/>
        <stop offset="1" stop-color="#e4e7ea"/>
      </linearGradient>
      <linearGradient id="swoosh" x1="0" y1="0" x2="1" y2="0">
        <stop offset="0" stop-color="var(--blue-bright)"/>
        <stop offset=".5" stop-color="var(--blue-mid)"/>
        <stop offset="1" stop-color="var(--blue-deep)"/>
      </linearGradient>
      <linearGradient id="footBlue" x1="0" y1="0" x2="1" y2="0">
        <stop offset="0" stop-color="var(--blue-deep)"/>
        <stop offset="1" stop-color="var(--blue-bright)"/>
      </linearGradient>
    </defs>

    <!-- blue headline swoosh -->
    <path d="M520 0 H1009 V404 C860 452 700 484 490 490 Z" fill="#7fb6e8" opacity=".55"/>
    <path d="M500 0 H1009 V392 C860 440 700 474 480 478 Z" fill="url(#swoosh)"/>

    <!-- hero photo area -->
    <path role="img" aria-label="Photo: technician in a white protective suit spraying disinfectant in an office"
          d="M0 0 H540 C630 120 640 300 540 440 C430 520 200 560 0 560 Z" fill="url(#photoTone)"/>

    <!-- team photo ring -->
    <circle role="img" aria-label="Photo: cleaning team in green uniforms mopping and wiping a room"
            cx="172" cy="436" r="124" fill="url(#teamTone)" stroke="var(--green)" stroke-width="14"/>
    <circle cx="337" cy="541" r="46" fill="var(--blue-mid)" opacity=".85"/>

    <!-- footer bands -->
    <path d="M0 1106 H500 L470 1200 H0 Z" fill="url(#footBlue)"/>
    <path d="M500 1106 H1009 V1200 H470 Z" fill="var(--green)"/>
    <path d="M560 1080 H972 L986 1134 H548 Z" fill="var(--blue-deep)"/>
  </svg>

  <h1 class="brand-title">Larkmoor<br>Cleaning &amp;<br>Disinfecting</h1>
  <div class="brand-rule"></div>
  <p class="tagline">Because your standards<br>aren't standard.</p>

  <p class="goal">Infection control is our ultimate goal</p>
  <p class="goal-note">We adhere to ALL NVB guidelines for both residential and commercial cleaning.</p>

  <section class="service-column commercial">
    <div class="column-head">
      <svg width="400" height="44" viewBox="0 0 400 44">
        <path d="M60 4 H378 L400 44 H60 Z" fill="var(--green)"/>
        <rect x="12" y="-10" width="58" height="54" rx="3" fill="var(--blue-mid)"/>
      </svg>
      <h2>Comercional</h2>
    </div>
    <ul class="service-list commercial-list">
      <li><span class="tick"><svg width="16" height="16" viewBox="0 0 16 16"><path d="M2 8 L6 12 L14 3" fill="none" stroke="#1c6fc0" stroke-width="2.6"/></svg></span>Janitorial</li>
      <li><span class="tick"><svg width="16" height="16" viewBox="0 0 16 16"><path d="M2 8 L6 12 L14 3" fill="none" stroke="#1c6fc0" stroke-width="2.6"/></svg></span>Offices</li>
      <li><span class="tick"><svg width="16" height="16" viewBox="0 0 16 16"><path d="M2 8 L6 12 L14 3" fill="none" stroke="#1c6fc0" stroke-width="2.6"/></svg></span>Floor maintenance</li>
      <li><span class="tick"><svg width="16" height="16" viewBox="0 0 16 16"><path d="M2 8 L6 12 L14 3" fill="none" stroke="#1c6fc0" stroke-width="2.6"/></svg></span>Carpet cleaning</li>
      <li><span class="tick"><svg width="16" height="16" viewBox="0 0 16 16"><path d="M2 8 L6 12 L14 3" fill="none" stroke="#1c6fc0" stroke-width="2.6"/></svg></span>Move-ins</li>
      <li><span class="tick"><svg width="16" height="16" viewBox="0 0 16 16"><path d="M2 8 L6 12 L14 3" fill="none" stroke="#1c6fc0" stroke-width="2.6"/></svg></span>Move-outs</li>
      <li><span class="tick"><svg width="16" height="16" viewBox="0 0 16 16"><path d="M2 8 L6 12 L14 3" fill="none" stroke="#1c6fc0" stroke-width="2.6"/></svg></span>Constructions clean-ups</li>
      <li><span class="tick"><svg width="16" height="16" viewBox="0 0 16 16"><path d="M2 8 L6 12 L14 3" fill="none" stroke="#1c6fc0" stroke-width="2.6"/></svg></span>Estate clean-outs</li>
    </ul>
  </section>

  <div class="column-divider"></div>

  <section class="service-column residential">
    <div class="column-head">
      <svg width="408" height="44" viewBox="0 0 408 44">
        <path d="M40 4 H386 L408 44 H40 Z" fill="var(--green)"/>
        <rect x="0" y="-10" width="70" height="54" rx="3" fill="var(--blue-mid)"/>
      </svg>
      <h2>Residental</h2>
    </div>
    <ul class="service-list residential-list">
      <li><span class="tick"><svg width="16" height="16" viewBox="0 0 16 16"><path d="M2 8 L6 12 L14 3" fill="none" stroke="#1c6fc0" stroke-width="2.6"/></svg></span>House cleaning</li>
      <li><span class="tick"><svg width="16" height="16" viewBox="0 0 16 16"><path d="M2 8 L6 12 L14 3" fill="none" stroke="#1c6fc0" stroke-width="2.6"/></svg></span>Before and after party</li>
      <li><span class="tick"><svg width="16" height="16" viewBox="0 0 16 16"><path d="M2 8 L6 12 L14 3" fill="none" stroke="#1c6fc0" stroke-width="2.6"/></svg></span>Move-ins</li>
      <li><span class="tick"><svg width="16" height="16" viewBox="0 0 16 16"><path d="M2 8 L6 12 L14 3" fill="none" stroke="#1c6fc0" stroke-width="2.6"/></svg></span>Move-outs</li>
      <li><span class="tick"><svg width="16" height="16" viewBox="0 0 16 16"><path d="M2 8 L6 12 L14 3" fill="none" stroke="#1c6fc0" stroke-width="2.6"/></svg></span>Holiday cleaning</li>
      <li><span class="tick"><svg width="16" height="16" viewBox="0 0 16 16"><path d="M2 8 L6 12 L14 3" fill="none" stroke="#1c6fc0" stroke-width="2.6"/></svg></span>Seasonal cleaning</li>
      <li><span class="tick"><svg width="16" height="16" viewBox="0 0 16 16"><path d="M2 8 L6 12 L14 3" fill="none" stroke="#1c6fc0" stroke-width="2.6"/></svg></span>Carpet cleaning</li>
      <li><span class="tick"><svg width="16" height="16" viewBox="0 0 16 16"><path d="M2 8 L6 12 L14 3" fill="none" stroke="#1c6fc0" stroke-width="2.6"/></svg></span>Deodorizing and sanitizing</li>
    </ul>
  </section>

  <p class="credentials">UMRE trained. Owned and operated by a licensed BSN Registered Nurse specially trained in Infection Control Prevention with over 25 years experience. Over two decades in Ambulatory Surgery Center Administration, Director of Nursing and Infection Control Prevention ad Consulting. Concentration and expertise in targeting Covid 19 and other transmissible pathogens.</p>

  <p class="website">www.larkmoorclean.com</p>
  <p class="estimate">Call us now for a free estimate!</p>
  <p class="call">
    <span>CALL US</span>
    <svg width="26" height="34" viewBox="0 0 26 34" aria-hidden="true">
      <rect x="3" y="2" width="20" height="30" rx="4" fill="none" stroke="#fff" stroke-width="3"/>
      <rect x="9" y="26" width="8" height="2.5" fill="#fff"/>
    </svg>
    <span class="number">0198 765 432</span>
  </p>
</main>
</body>
</html>
```